Quillo App - Live Events Stream

Need mobile first appliation designs for a new location based events and offers application <br/><br/>Will require at least 5 screens creating, namely:<br/><br/>- Landing screen<br/>- Event/Offer listings screen<br/>- Overview of Event/Offer screen<br/>- Chat/Stream for Event/Offer<br/>- Directions for Event/Offer<br/>- Create Event/Offer screen(s)<br/><br/>Will require the design to have a google material feel. <br/><br/>See Attached files for further details

Requirements
Must have
• See Doc
Nice to have
• See Doc
Should not have
• See Doc

```html
<!DOCTYPE html>
<html lang="en">
<head>
<meta charset="utf-8">
<title>Quillo App - Live Events Stream</title>
<link href="https://fonts.googleapis.com/css2?family=Arimo:wght@400;700&display=swap" rel="stylesheet">
<style>
:root{
  --bg:#e9e9ea;
  --paper:#ffffff;
  --yellow:#e8d85a;
  --teal:#6dcfd3;
  --teal-dark:#4fb9bf;
  --pink:#de90dc;
  --pink-dark:#cf72cc;
  --ink:#2f2f2f;
  --muted:#777;
  --line:#c9c9c9;
  --star:#f0cf3a;
}
*{box-sizing:border-box;margin:0;padding:0}
html,body{width:1200px;height:609px;overflow:hidden}
body{background:var(--bg);font-family:"Arimo",Arial,sans-serif;color:var(--ink);position:relative}
.abs{position:absolute}
.screen{position:absolute;background:var(--paper);box-shadow:0 1px 3px rgba(0,0,0,.15)}
.home{left:50px;top:58px;width:232px;height:490px;border-radius:26px}
.panel{width:252px;height:506px}
.brand{position:absolute;left:0;width:100%;text-align:center;font-weight:700;font-size:34px;color:var(--ink);letter-spacing:.5px}
.band{position:absolute;left:0;width:100%;height:35px;background:var(--yellow);color:#fff;font-weight:700;font-size:15px;line-height:35px;text-align:center;letter-spacing:.3px}
.tile{position:absolute;left:77px;width:184px;height:91px;border-radius:3px;color:#fff;font-weight:700;font-size:17px;line-height:22px;text-align:center}
.tile-events{top:170px;background:linear-gradient(var(--teal),var(--teal-dark))}
.tile-chat{top:298px;background:linear-gradient(var(--pink),var(--pink-dark))}
.tile-badge{position:absolute;width:54px;height:54px;border-radius:50%;left:142px}
.tile-text{position:absolute;left:0;width:100%}
.btn{position:absolute;left:73px;width:189px;height:33px;border:1.5px solid var(--teal);color:var(--teal);font-weight:700;font-size:12.5px;line-height:30px;text-align:center;background:#fff}
.btn-login{border:none;background:linear-gradient(#eedc5a,#e2c92f);color:#fff;line-height:33px}
.avatar{position:absolute;width:32px;height:32px;border-radius:50%;background:radial-gradient(circle at 50% 40%,#d9a888,#8a5d45)}
.bubble{position:absolute;width:160px;border-radius:3px;color:#fff;font-size:9px;line-height:11px;padding:9px 9px 0 18px}
.bubble-in{background:var(--teal)}
.bubble-out{background:var(--pink);text-align:right;padding:9px 18px 0 12px}
.bubble .name{font-weight:700;font-size:10.5px;margin-bottom:4px}
.bubble .time{position:absolute;top:9px;font-size:6.5px;font-weight:700}
.bubble-in .time{right:5px}
.bubble-out .time{left:10px}
.bubble-in::before,.bubble-out::after{content:"";position:absolute;top:12px;border:6px solid transparent}
.bubble-in::before{left:-11px;border-right-color:var(--teal)}
.bubble-out::after{right:-11px;border-left-color:var(--pink)}
.compose{position:absolute;left:336px;top:504px;width:221px;height:32px;border:1px solid var(--line);font-size:10.5px;color:var(--muted);line-height:30px;padding-left:31px}
.photo{position:absolute;left:612px;top:159px;width:224px;height:155px;background:linear-gradient(180deg,#2d4a66 0%,#6b7d8c 35%,#c99d5a 60%,#2f3a2a 100%)}
.arrow{position:absolute;top:55px;width:30px;height:44px}
.t{position:absolute;font-size:11px;white-space:nowrap}
.count{position:absolute;top:419px;width:29px;height:26px;background:var(--teal);color:#fff;text-align:center;font-weight:700;font-size:12px;line-height:13px;padding-top:2px}
.count small{display:block;font-size:6.5px;font-weight:400;line-height:8px}
.field{position:absolute;left:892px;width:209px;height:32px;border:1px solid var(--line);font-size:11.5px;line-height:30px;padding-left:37px;color:var(--ink)}
.field svg{position:absolute;left:11px;top:8px}
.field.plain{padding-left:13px}
.filter{position:absolute;left:893px;top:447px;width:208px;height:38px;background:linear-gradient(#e9a3e6,var(--pink-dark));color:#fff;font-weight:700;font-size:15px;text-align:center;line-height:38px}
</style>
</head>
<body>

<!-- Home screen -->
<section class="screen home" aria-label="Landing screen">
  <div class="brand" style="top:36px">Quillo</div>
</section>
<div class="tile tile-events"><div class="tile-text" style="top:37px">Latest and<br>Nearest Events</div></div>
<svg class="tile-badge abs" style="top:143px" viewBox="0 0 54 54"><circle cx="27" cy="27" r="27" fill="#6dcfd3"/><path d="M27 46 C20 35 16 30 16 23 a11 11 0 0 1 22 0 c0 7-4 12-11 23z" fill="none" stroke="#fff" stroke-width="2.5"/><circle cx="27" cy="23" r="4.5" fill="none" stroke="#fff" stroke-width="2.5"/></svg>
<div class="tile tile-chat"><div class="tile-text" style="top:42px">Latest Chat<br><span style="font-size:15px">/Images from stream</span></div></div>
<svg class="tile-badge abs" style="top:271px" viewBox="0 0 54 54"><circle cx="27" cy="27" r="27" fill="#e39be0"/><path d="M15 27 a12 10 0 1 1 6 8.5 l-6 3 2-6z" fill="none" stroke="#fff" stroke-width="2.2"/><path d="M21 22h12M21 26h12M21 30h8" stroke="#fff" stroke-width="2"/></svg>
<div class="btn" style="top:409px">START AN EVENT</div>
<div class="btn" style="top:449px">SEARCH FOR EVENTS</div>
<div class="btn btn-login" style="top:488px">LOGIN</div>

<!-- Live chat -->
<section class="screen panel" style="left:320px;top:40px" aria-label="Live chat screen">
  <div class="brand" style="top:14px">Quillo</div>
  <div class="band" style="top:68px">LIVE CHAT</div>
</section>
<div class="avatar" role="img" aria-label="User avatar photo" style="left:341px;top:165px"></div>
<div class="bubble bubble-in" style="left:385px;top:160px;height:81px"><span class="time">1 min ago</span><div class="name">Mara Lind</div>Curabitur vel dolor ultrices ipsum dictum tristique Praesent vitae lacus Ut velit enim estib ulum non fermentum nec</div>
<div class="avatar" role="img" aria-label="User avatar photo" style="left:518px;top:268px"></div>
<div class="bubble bubble-out" style="left:346px;top:264px;height:80px"><span class="time">2 min ago</span><div class="name">Theo Brandt</div>Curabitur vel dolor ultrices ipsum dictum tristique Praesent vitae lacus Ut velit enim estib ulum non fermentum nec</div>
<div class="avatar" role="img" aria-label="User avatar photo" style="left:341px;top:363px"></div>
<div class="bubble bubble-in" style="left:385px;top:357px;height:62px"><span class="time">2 min ago</span><div class="name">Mara Lind</div>Curabitur vel dolor ultrices ipsum dictum tristique Praesent</div>
<div class="avatar" role="img" aria-label="User avatar photo" style="left:518px;top:439px"></div>
<div class="bubble bubble-out" style="left:346px;top:434px;height:56px"><span class="time">2 min ago</span><div class="name">Author Name</div>Curabitur vel dolor ultrices ipsum dictum tristique Praesent</div>
<div class="compose">Type a Message
  <svg class="abs" style="left:8px;top:7px" width="17" height="17" viewBox="0 0 17 17"><circle cx="8.5" cy="8.5" r="7.5" fill="none" stroke="#aaa" stroke-width="1.2"/><circle cx="6" cy="7" r="1" fill="#aaa"/><circle cx="11" cy="7" r="1" fill="#aaa"/><path d="M5 10.5q3.5 3 7 0" fill="none" stroke="#aaa" stroke-width="1.2"/></svg>
  <svg class="abs" style="right:9px;top:8px" width="17" height="14" viewBox="0 0 17 14"><rect x="0" y="2.5" width="17" height="11.5" rx="1.5" fill="#999"/><rect x="5" y="0" width="7" height="4" fill="#999"/><circle cx="8.5" cy="8" r="3.2" fill="#fff"/></svg>
</div>

<!-- Event overview -->
<section class="screen panel" style="left:597px;top:38px" aria-label="Event overview screen">
  <div class="brand" style="top:14px">Quillo</div>
  <div class="band" style="top:68px">EVENT OVERVIEW</div>
</section>
<div class="photo" role="img" aria-label="Photo of an outdoor evening event under a lit marquee tent">
  <svg class="arrow" style="left:2px" viewBox="0 0 30 44"><path d="M20 12 L10 22 L20 32" fill="none" stroke="#fff" stroke-width="3"/></svg>
  <svg class="arrow" style="right:2px" viewBox="0 0 30 44"><path d="M10 12 L20 22 L10 32" fill="none" stroke="#fff" stroke-width="3"/></svg>
</div>
<div class="t" style="left:617px;top:329px;font-size:16px;font-weight:700">Event Title here</div>
<div class="t" style="left:616px;top:355px">Popularity
  <svg style="vertical-align:-2px;margin-left:6px" width="68" height="12" viewBox="0 0 68 12"><g fill="#f0cf3a"><path id="s" d="M6 0l1.8 3.9 4.2.5-3.1 2.9.8 4.2L6 9.4 2.3 11.5l.8-4.2L0 4.4l4.2-.5z"/><use href="#s" x="14"/><use href="#s" x="28"/><use href="#s" x="42"/><use href="#s" x="56"/></g></svg>
</div>
<div class="t" style="left:616px;top:380px">Event Start: Soon</div>
<div class="t" style="left:736px;top:379px">Category Title</div>
<div class="t" style="left:617px;top:403px">Event Ends:</div>
<div class="t" style="left:737px;top:405px">Attendees: 250</div>
<div class="count" style="left:617px">05<small>Hours</small></div>
<div class="count" style="left:652px">15<small>Mins</small></div>
<div class="count" style="left:686px">30<small>Secs</small></div>
<div class="t" style="left:737px;top:427px">Likes:
  <svg style="vertical-align:-2px;margin:0 5px" width="17" height="15" viewBox="0 0 17 15"><rect x="0" y="6" width="4" height="9" fill="#de90dc"/><path d="M5 6l4-6c2 0 2 2 1.5 4H16c1 0 1 1.5.6 2.5L14.5 14H5z" fill="#de90dc"/></svg>110</div>
<svg class="abs" style="left:617px;top:459px" width="11" height="15" viewBox="0 0 11 15"><path d="M5.5 15C2 10 0 7.5 0 5.5a5.5 5.5 0 0 1 11 0C11 7.5 9 10 5.5 15z" fill="#de90dc"/><circle cx="5.5" cy="5.5" r="2" fill="#fff"/></svg>
<div class="t" style="left:629px;top:458px;font-size:10px;line-height:13px">42 Linden Avenue<br>#B Oakvale 20417</div>
<svg class="abs" style="left:736px;top:457px" width="16" height="13" viewBox="0 0 16 13"><path d="M8 0c4.4 0 8 2.4 8 5.4S12.4 10.8 8 10.8c-.8 0-1.6-.1-2.3-.2L1 13l1.5-3.3C.9 8.7 0 7.1 0 5.4 0 2.4 3.6 0 8 0z" fill="#de90dc"/></svg>
<div class="t" style="left:754px;top:456px">Chat Stream</div>
<div class="t" style="left:629px;top:489px;text-decoration:underline">Direction</div>

<!-- Event search -->
<section class="screen panel" style="left:871px;top:39px" aria-label="Event search screen">
  <div class="brand" style="top:14px">Quillo</div>
  <div class="band" style="top:69px">EVENT SEARCH</div>
</section>
<div class="field" style="top:163px"><svg width="14" height="16" viewBox="0 0 14 16"><path d="M7 16C3 11 1 8.5 1 6a6 6 0 0 1 12 0c0 2.5-2 5-6 10z" fill="#aaa"/><circle cx="7" cy="6" r="2.2" fill="#fff"/></svg>Location</div>
<div class="field" style="top:202px"><svg width="20" height="16" viewBox="0 0 20 16"><circle cx="2.5" cy="8" r="2" fill="none" stroke="#aaa" stroke-width="1.3"/><circle cx="17.5" cy="8" r="2" fill="none" stroke="#aaa" stroke-width="1.3"/><path d="M4.5 8h11" stroke="#aaa" stroke-width="1.5"/></svg>Distance</div>
<div class="field" style="top:241px"><svg width="18" height="16" viewBox="0 0 18 16"><g fill="#aaa"><circle cx="4" cy="5" r="2.5"/><circle cx="14" cy="5" r="2.5"/><circle cx="9" cy="6" r="3"/><path d="M0 12c0-3 2-4 4-4s3 1 3 2v3H0zM18 12c0-3-2-4-4-4s-3 1-3 2v3h7zM4 16c0-4 2.5-6 5-6s5 2 5 6z"/></g></svg>Friends</div>
<div class="field" style="top:280px"><svg width="17" height="16" viewBox="0 0 17 16"><path d="M0 3h17M0 8h17M0 13h17" stroke="#aaa" stroke-width="1.8"/></svg>Categories</div>
<div class="field" style="top:320px"><svg width="16" height="16" viewBox="0 0 16 16"><circle cx="8" cy="8" r="7" fill="none" stroke="#aaa" stroke-width="1.5"/><path d="M8 4v4.5h-3" fill="none" stroke="#aaa" stroke-width="1.5"/></svg>Starting Time
  <svg class="abs" style="left:auto;right:12px;top:12px" width="13" height="8" viewBox="0 0 13 8"><path d="M1 1l5.5 5.5L12 1" fill="none" stroke="#555" stroke-width="1.8"/></svg></div>
<div class="field plain" style="top:359px">No. of offeres</div>
<div class="field plain" style="top:398px">No.of attendees</div>
<div class="filter">FILTER</div>

</body>
</html>
```